Software Company Requires Website

We need a web design for a new mobile software development company based in London named Velquin Solutions.
The design needs to be clean and smooth. Not too flashy, not too boring.
I would like to try the design with some warm colors, and maybe a headline or something highlighted with a strong color. ( logo ? ) The layout should be something like the bellow links, all in one page.

http://brantelo.net/
http://www.kelvory.com/
http://www.work-plover.de/
http://www.tusker.com/
http://www.quildenta.com/us/

Now some of them they seem different from the others, but in each of them there is something that ticks my brain, so it`s up to you to surprise me.

I have uploaded the logo of the company, so you guys can fit that in your design as well.
Updates

Hy everybody This will be the last update for the brief. The company will focus in the beginning for mobile development only, so i would like the website design to be done in a matter that will reflect that. We will develop IOS, Android and Windows applications. We will also require 3 pages: One for the home menu, one for portfolio and one for contact us. The layout should be the same ( one page scroll down ) but the design of the 3 pages different. Please readdress the brief. Hope that i provided enough information for the scope of the project.

I have uploaded the logo that you guys can use. If the logo requires small modifications you can adjust that to suit your idea as long as the logo does not change completely.

Target Market(s)

High End companies that require simplified software solutions.

Industry/Entity Type

It Company

Number of Pages Required

3 page

Requirements
Must have
• One page scroll down layout for 3 pages:
• one for home page, one for portfolio and one for contact us.
• In the portfolio page we would like to have different display options for given examples of applications ( min 3 )

```html
<!DOCTYPE html>
<html lang="en">
<head>
<meta charset="utf-8">
<title>Velquin Solutions</title>
<link href="https://fonts.googleapis.com/css2?family=Roboto+Slab:wght@400;700&family=Roboto:wght@400;500;700&display=swap" rel="stylesheet">
<style>
:root{
  --orange:#e3672a;
  --orange-dark:#a9441a;
  --orange-light:#f39a4e;
  --amber:#e8a030;
  --amber-dark:#a86a14;
  --coral:#d9503c;
  --coral-dark:#9c3325;
  --hero-top:#f2a25a;
  --hero-bottom:#c85424;
  --ink:#2d2d2d;
  --muted:#6c6c6c;
  --night:#211c19;
  --night-2:#3a302a;
  --brown:#3a1f12;
  --white:#ffffff;
}
*{box-sizing:border-box;margin:0;padding:0}
html,body{width:1200px;height:3697px;overflow:hidden}
body{font-family:'Roboto',sans-serif;color:var(--ink);background:var(--white);position:relative}

/* three pages stacked on one scroll, each with its own accent */
.page-home{--accent:var(--orange);--accent-dark:var(--orange-dark);--accent-light:var(--orange-light)}
.page-portfolio{--accent:var(--amber);--accent-dark:var(--amber-dark);--accent-light:#f4c06a}
.page-contact{--accent:var(--coral);--accent-dark:var(--coral-dark);--accent-light:#ec7d68}

.section{position:absolute;left:0;width:1200px;overflow:hidden}
.heading{font-family:'Roboto Slab',serif;font-weight:700;font-size:30px;text-align:center;color:var(--accent);position:absolute;left:0;width:100%}
.heading::after{content:"";display:block;width:110px;height:3px;background:var(--accent);margin:8px auto 0}
.heading.light{color:var(--white)}
.btn{display:inline-block;background:var(--accent);color:var(--white);font-size:9px;font-weight:700;padding:5px 12px;text-decoration:none}

/* hero */
.hero{top:0;height:598px;background:linear-gradient(160deg,var(--hero-top),var(--hero-bottom))}
.hero-photo{position:absolute;inset:0;background:radial-gradient(ellipse at 75% 35%,rgba(255,240,220,.3),transparent 55%),radial-gradient(ellipse at 20% 80%,rgba(120,40,10,.3),transparent 60%)}
.brand{position:absolute;left:269px;top:18px;display:flex;align-items:center;gap:10px;color:var(--white);font-family:'Roboto Slab',serif;font-size:26px;font-weight:700}
.brand-mark{width:26px;height:26px;border:2px solid var(--white);border-radius:50%}
.nav{position:absolute;left:625px;top:30px;display:flex;gap:6px}
.nav a{color:var(--white);text-decoration:none;font-size:11px;font-weight:500;letter-spacing:.5px;padding:5px 10px}
.nav a.active{background:var(--white);color:var(--orange-dark)}
.hero-title{position:absolute;top:268px;left:0;width:100%;text-align:center;color:var(--white);font-family:'Roboto Slab',serif;font-weight:700;font-size:36px;line-height:46px}
.hero-title .hl{color:#ffe3b8}
.hero-more{position:absolute;top:528px;left:0;width:100%;text-align:center;color:var(--white);font-size:11px;letter-spacing:1px}

/* services */
.services{top:598px;height:450px;background:var(--white)}
.services .heading{top:62px}
.service-list{position:absolute;top:166px;left:269px;display:flex;gap:10px}
.service{width:161px;height:160px;background:var(--accent-dark);color:var(--white);text-align:center;padding-top:12px;position:relative}
.service-icon{width:44px;height:44px;border-radius:50%;background:var(--white);margin:0 auto;display:flex;align-items:center;justify-content:center}
.service h3{font-family:'Roboto Slab',serif;font-size:15px;margin:7px 0 4px}
.service p{font-size:8px;line-height:11px;padding:0 18px;opacity:.9}
.service .btn{position:absolute;bottom:10px;left:50%;transform:translateX(-50%);background:var(--accent-light)}

/* about */
.about{top:1048px;height:582px;background:linear-gradient(180deg,var(--night),var(--night-2) 50%,var(--night))}
.about .heading{top:78px}
.about-text{position:absolute;top:138px;left:269px;width:665px;color:#ece6e1;font-size:9.5px;line-height:13px}
.about-text p{margin-bottom:11px}

/* portfolio */
.portfolio{top:1630px;height:570px;background:linear-gradient(135deg,#5a3a26,#3a2418 55%,#7a5236)}
.portfolio .heading{top:56px}
.work-grid{position:absolute;top:150px;left:269px;display:grid;grid-template-columns:repeat(4,161px);gap:33px 7px}
.work-shot{height:102px}
.work-caption{background:var(--accent-dark);color:var(--white);height:60px;padding:6px 8px}
.work-caption h4{font-size:10px;font-weight:700}
.work-caption p{font-size:8px;line-height:11px;margin-top:3px;opacity:.9}

/* team */
.team{top:2200px;height:488px;background:var(--white)}
.team .heading{top:68px}
.member{position:absolute;top:168px;width:160px;text-align:center}
.member-photo{width:116px;height:116px;border-radius:50%;margin:0 auto;background:linear-gradient(160deg,#d6cdc6,#8a7d73);border:4px solid #eee8e3}
.member h4{font-size:11px;margin-top:8px}
.member .role{font-size:8px;color:var(--muted)}
.member p{font-size:8px;line-height:11px;color:var(--muted);margin:5px 8px 6px}
.member .btn{background:var(--accent-dark);padding:5px 10px}

/* map */
.map{top:2688px;height:270px;background:linear-gradient(110deg,#ece5d8 0%,#f3eee4 45%,#e9c9a4 60%,#d8dcc2 75%,#e3c4a0 100%)}

/* contact */
.contact{top:2958px;height:504px;background:linear-gradient(180deg,#1d1815,#2f2722 60%,#1a1613)}
.contact .heading{top:80px}
.contact-info{position:absolute;top:185px;left:269px;width:370px;color:#e0d8d2}
.contact-info h5{font-size:12px;color:var(--white);margin-bottom:6px}
.contact-info > p{font-size:8.5px;line-height:12px}
.info-row{display:flex;align-items:center;gap:10px;margin-top:14px;font-size:8.5px;line-height:12px}
.info-icon{width:24px;height:24px;border-radius:50%;background:var(--white);display:flex;align-items:center;justify-content:center;flex:none}
.contact-form{position:absolute;top:185px;left:665px;width:269px;display:flex;flex-direction:column;gap:8px}
.field{background:var(--white);height:26px;font-size:9px;color:#999;padding:7px 8px}
.field.area{height:90px}
.send{background:var(--accent);color:var(--white);height:26px;text-align:center;font-size:10px;font-weight:700;padding-top:7px}

/* footer */
.social{top:3462px;height:174px;background:var(--coral);display:flex;justify-content:center;align-items:center;gap:10px}
.social-dot{width:36px;height:36px;border-radius:50%;border:2px solid var(--white)}
.legal{top:3636px;height:61px;background:var(--brown);color:#e6d2c4;font-size:9px}
.legal .left{position:absolute;left:269px;top:25px}
.legal .right{position:absolute;right:266px;top:25px}
</style>
</head>
<body>

<div class="page page-home" id="home">
<header class="section hero">
  <div class="hero-photo" role="img" aria-label="Photo of hands using a tablet showing business charts, tinted warm orange"></div>
  <div class="brand"><span class="brand-mark"></span>Velquin</div>
  <nav class="nav">
    <a class="active" href="#home">HOME</a><a href="#about">ABOUT US</a><a href="#services">SERVICES</a><a href="#portfolio">PORTFOLIO</a><a href="#team">TEAM</a><a href="#contact">CONTACT</a>
  </nav>
  <h1 class="hero-title">"Our mission is to create <span class="hl">cutting-edge</span><br>IT Solutions to our clients and partners."</h1>
  <div class="hero-more">MORE</div>
</header>

<section class="section services" id="services">
  <h2 class="heading">Featured Services</h2>
  <div class="service-list">
    <div class="service">
      <div class="service-icon"><svg width="26" height="18" viewBox="0 0 26 18"><path d="M6 17a5 5 0 0 1 0-10 7 7 0 0 1 13-1 5.5 5.5 0 0 1 1 11z" fill="none" stroke="#a9441a" stroke-width="2"/></svg></div>
      <h3>Cloud</h3>
      <p>Secure hosting and sync services that scale with your mobile apps.</p>
      <a class="btn" href="#">Read More</a>
    </div>
    <div class="service">
      <div class="service-icon"><svg width="26" height="22" viewBox="0 0 26 22"><circle cx="9" cy="7" r="4" fill="#a9441a"/><circle cx="18" cy="8" r="3" fill="#a9441a"/><path d="M1 21c0-6 16-6 16 0zM14 21c1-4 11-5 11 0z" fill="#a9441a"/></svg></div>
      <h3>Our Team</h3>
      <p>Skilled engineers and designers focused on clean, reliable products.</p>
      <a class="btn" href="#">Read More</a>
    </div>
    <div class="service">
      <div class="service-icon"><svg width="24" height="22" viewBox="0 0 24 22"><rect x="1" y="5" width="22" height="15" rx="2" fill="none" stroke="#a9441a" stroke-width="2"/><path d="M8 5V2h8v3" fill="none" stroke="#a9441a" stroke-width="2"/></svg></div>
      <h3>Projects</h3>
      <p>Apps delivered for iOS, Android and Windows across many sectors.</p>
      <a class="btn" href="#">Read More</a>
    </div>
    <div class="service">
      <div class="service-icon"><svg width="24" height="24" viewBox="0 0 24 24"><rect x="6" y="6" width="12" height="12" fill="none" stroke="#a9441a" stroke-width="2"/><path d="M9 2v4M15 2v4M9 18v4M15 18v4M2 9h4M2 15h4M18 9h4M18 15h4" stroke="#a9441a" stroke-width="2"/></svg></div>
      <h3>Technology</h3>
      <p>Modern tools and frameworks chosen to keep every build fast.</p>
      <a class="btn" href="#">Read More</a>
    </div>
  </div>
</section>

<section class="section about" id="about" role="img" aria-label="Dark photo of an open-plan office with desks and monitors">
  <h2 class="heading light">About Us</h2>
  <div class="about-text">
    <p>Velquin Solutions is a London studio building mobile software for companies that want simple tools done well. We plan, design and ship native apps for iOS, Android and Windows, and we support them long after launch. Every project starts with a short discovery phase where we learn how your people work, which tasks slow them down and where a mobile app can save real time. From there we shape clear screens, write careful code and test on real devices before release, so the first version your staff open already feels familiar and dependable. We keep documentation tidy and hand over everything you need to own the product with confidence.</p>
    <p>Our team keeps projects small, focused and honest. You speak directly with the people building your product, you see progress every week and you get clear estimates before each stage. We believe good software should feel calm to use, so we remove clutter, keep flows short and make sure each screen has one clear purpose. Security, speed and accessibility are part of every build rather than extras added at the end. Each release passes through automated checks, manual review and a short pilot with real users, which lets us catch small problems early and keep quality steady from one version to the next.</p>
    <p>We work with high end clients across finance, retail, logistics and health, helping them turn complex processes into light mobile experiences. A sales team might need instant access to stock levels, a clinic may want simple bookings, and a warehouse could benefit from fast scanning tools. In each case we look for the shortest path between a task and its result, then design an app around that path. Our engineers know the details of each platform, so apps feel native on every phone and tablet while sharing a common core that keeps maintenance costs low over the years ahead.</p>
    <p>Beyond building apps, we offer ongoing care plans that cover updates for new operating system versions, performance monitoring, analytics reviews and small feature improvements. Many of our clients have worked with us for several years, growing their products step by step as their business changes. Whether you need a new app, a redesign of an existing one or a partner to maintain your products, we are ready to help. Get in touch and tell us about your idea, and we will come back with honest advice, a clear plan and a realistic timeline for delivering it.</p>
  </div>
</section>
</div>

<div class="page page-portfolio" id="portfolio">
<section class="section portfolio" role="img" aria-label="Warm-toned photo of a businessman touching a digital interface">
  <h2 class="heading light">Our Portfolio</h2>
  <div class="work-grid">
    <div><div class="work-shot" style="background:linear-gradient(135deg,#b8693a,#e8c29c)" role="img" aria-label="Project photo of a team at a laptop"></div><div class="work-caption"><h4>Project Title 1</h4><p>Field service app for a logistics group.</p></div></div>
    <div><div class="work-shot" style="background:linear-gradient(135deg,#e2d8cf,#b49a84)" role="img" aria-label="Project photo of people in a meeting"></div><div class="work-caption"><h4>Project Title 2</h4><p>Booking tool for a private health clinic.</p></div></div>
    <div><div class="work-shot" style="background:linear-gradient(135deg,#eae2da,#b8a391)" role="img" aria-label="Project photo of an office workspace"></div><div class="work-caption"><h4>Project Title 3</h4><p>Sales dashboard for a retail chain.</p></div></div>
    <div><div class="work-shot" style="background:linear-gradient(135deg,#7a6a3f,#c9b98a)" role="img" aria-label="Project photo of a keyboard with a highlighted key"></div><div class="work-caption"><h4>Project Title 4</h4><p>Payments app for a finance startup.</p></div></div>
    <div><div class="work-shot" style="background:linear-gradient(135deg,#f0c28e,#b86a30)" role="img" aria-label="Project illustration of cloud devices"></div><div class="work-caption"><h4>Project Title 5</h4><p>Cloud sync service for remote teams.</p></div></div>
    <div><div class="work-shot" style="background:linear-gradient(135deg,#9a4e26,#dd9f6e)" role="img" aria-label="Project image of a padlock on a circuit"></div><div class="work-caption"><h4>Project Title 6</h4><p>Secure messaging app for a bank.</p></div></div>
    <div><div class="work-shot" style="background:linear-gradient(135deg,#f3b24a,#8a4a1c)" role="img" aria-label="Project photo of a sunset skyline"></div><div class="work-caption"><h4>Project Title 7</h4><p>Travel guide app for city visitors.</p></div></div>
    <div><div class="work-shot" style="background:linear-gradient(135deg,#665448,#c2ada0)" role="img" aria-label="Project photo of a hand on a tablet"></div><div class="work-caption"><h4>Project Title 8</h4><p>Inventory scanner for a warehouse.</p></div></div>
  </div>
</section>

<section class="section team" id="team">
  <h2 class="heading">Our Team</h2>
  <div class="member" style="left:263px"><div class="member-photo" role="img" aria-label="Portrait photo of a team member"></div><h4>Mr Halvard</h4><div class="role">Founder</div><p>Leads strategy and client relations with over ten years in mobile.</p><a class="btn" href="#">Read Profile</a></div>
  <div class="member" style="left:434px"><div class="member-photo" role="img" aria-label="Portrait photo of a team member"></div><h4>Mr Teodric</h4><div class="role">Lead Developer</div><p>Builds native iOS and Android apps with a focus on speed.</p><a class="btn" href="#">Read Profile</a></div>
  <div class="member" style="left:609px"><div class="member-photo" role="img" aria-label="Portrait photo of a team member"></div><h4>Mr Orwen Falk</h4><div class="role">Designer</div><p>Shapes calm, clear interfaces that people enjoy using daily.</p><a class="btn" href="#">Read Profile</a></div>
  <div class="member" style="left:777px"><div class="member-photo" role="img" aria-label="Portrait photo of a team member"></div><h4>Mr Brisden Kale</h4><div class="role">Project Manager</div><p>Keeps every project on time and every client informed.</p><a class="btn" href="#">Read Profile</a></div>
</section>
</div>

<div class="page page-contact" id="contact">
<section class="section map" role="img" aria-label="Street map of the office area beside a river"></section>

<section class="section contact" role="img" aria-label="Dark photo of a desk with a laptop">
  <h2 class="heading light">Contact Us</h2>
  <div class="contact-info">
    <h5>CONTACT INFO</h5>
    <p>Have an idea for a mobile app? Send us a short note about your project and we will reply within one working day to arrange a call.</p>
    <div class="info-row"><span class="info-icon"><svg width="10" height="14" viewBox="0 0 10 14"><path d="M5 13S1 8 1 5a4 4 0 0 1 8 0c0 3-4 8-4 8z" fill="#211c19"/><circle cx="5" cy="5" r="1.5" fill="#fff"/></svg></span><span>14 Corvell Yard, Tamsworth Lane<br>London EC2 9QT, United Kingdom</span></div>
    <div class="info-row"><span class="info-icon"><svg width="12" height="12" viewBox="0 0 12 12"><circle cx="6" cy="6" r="5" fill="none" stroke="#211c19" stroke-width="1.5"/><path d="M6 3v3l2 1.5" fill="none" stroke="#211c19" stroke-width="1.5"/></svg></span><span>Office Hours: Mon – Fri, 9am – 6pm<br>Weekend: by appointment</span></div>
    <div class="info-row"><span class="info-icon"><svg width="12" height="12" viewBox="0 0 12 12"><path d="M2 1h3l1 3-2 1a7 7 0 0 0 3 3l1-2 3 1v3c-6 0-9-3-9-9z" fill="#211c19"/></svg></span><span>Tel: +44 20 7946 0381</span></div>
    <div class="info-row"><span class="info-icon"><svg width="12" height="10" viewBox="0 0 12 10"><rect x="1" y="1" width="10" height="8" fill="none" stroke="#211c19" stroke-width="1.5"/><path d="M1 1l5 4 5-4" fill="none" stroke="#211c19" stroke-width="1.5"/></svg></span><span>E-mail: hello@velquin.net</span></div>
  </div>
  <form class="contact-form">
    <div class="field">Your Name</div>
    <div class="field">Your Email</div>
    <div class="field">Subject</div>
    <div class="field area">Your Message</div>
    <div class="send">SEND</div>
  </form>
</section>

<footer class="section social" aria-label="Social links">
  <span class="social-dot"></span><span class="social-dot"></span><span class="social-dot"></span><span class="social-dot"></span><span class="social-dot"></span>
</footer>
<div class="section legal">
  <span class="left">Copyright © 2014 Velquin Solutions. All Rights Reserved.</span>
  <span class="right">Design &amp; Development by Velquin Studio</span>
</div>
</div>

</body>
</html>
```